Corvanti, LLC Website

Creating website for medical billing company.

Target Market(s)

Medical providers

Industry/Entity Type

Medical billing

Coding

Coded - Design and coding required

Number of Pages Required

3 page

Font styles to use
Other font styles liked:
• Fonts that match our logo.

Requirements
Must have
• First page (greeting and explanation of who we are). Second page something about me and company (I'll supply some content, make generic for now). And page three, information that people can give for us to contact them.
Nice to have
• A little animation. But not over-the-top. Colors that match our logo.
Should not have
• Over-the-top animation.

```html
<!DOCTYPE html>
<html lang="en">
<head>
<meta charset="utf-8">
<title>Corvanti, LLC – Medical Billing</title>
<link href="https://fonts.googleapis.com/css2?family=Montserrat:wght@400;500;600;700;800&family=Open+Sans:wght@400;600;700&display=swap" rel="stylesheet">
<style>
:root{
  --teal:#15a6bd;
  --teal-dark:#0e8ca1;
  --teal-light:#8fd7e3;
  --navy:#1d2f5e;
  --navy-deep:#172650;
  --ink:#1f2a3c;
  --text:#5d6675;
  --grey-bg:#f2f3f5;
  --footer:#0d0f12;
  --footer-bar:#16181c;
  --white:#ffffff;
}
*{margin:0;padding:0;box-sizing:border-box}
html,body{width:1200px;height:3320px;overflow:hidden}
body{font-family:'Open Sans',Arial,sans-serif;color:var(--text);background:var(--white);position:relative}
.head-font{font-family:'Montserrat',Arial,sans-serif}

/* top bar */
.topbar{height:48px;background:linear-gradient(90deg,var(--teal) 0%,var(--teal) 50%,var(--teal-dark) 100%);display:flex;align-items:center;padding:0 112px;color:var(--white);font-size:15px}
.topbar .contact{display:flex;align-items:center;gap:10px}
.topbar .sep{width:1px;height:18px;background:rgba(255,255,255,.6);margin:0 22px}
.topbar .social{margin-left:auto;display:flex;gap:10px}
.topbar .social span{width:24px;height:24px;border-radius:50%;background:rgba(255,255,255,.25);border:1px solid rgba(255,255,255,.7)}

/* nav */
.nav{height:112px;display:flex;align-items:center;padding:0 112px;background:var(--white)}
.logo{display:flex;align-items:center;gap:12px;font-family:'Montserrat',Arial,sans-serif;font-weight:700;font-size:26px;color:var(--navy)}
.logo .dot{width:34px;height:34px;border-radius:50%;background:var(--teal)}
.menu{margin-left:auto;display:flex;align-items:center;gap:40px;font-family:'Montserrat',Arial,sans-serif;font-weight:600;font-size:15px;color:var(--ink)}
.menu .active{color:var(--teal);position:relative}
.menu .active::after{content:"";position:absolute;left:-12px;right:-12px;top:-44px;height:4px;background:var(--teal)}
.menu svg{margin-left:10px}

/* hero */
.hero{position:relative;height:600px;background:linear-gradient(120deg,#c9e7ee 0%,#7ec6d6 35%,#3da9c0 65%,#1c8fa9 100%);overflow:hidden}
.hero::after{content:"";position:absolute;left:0;right:0;bottom:0;height:90px;background:linear-gradient(180deg,rgba(21,166,189,0) 0%,rgba(21,166,189,.55) 100%)}
.hero-text{position:absolute;left:112px;top:330px;color:var(--white);z-index:2}
.hero-text .pre{font-family:'Montserrat',Arial,sans-serif;font-size:36px;font-weight:400;letter-spacing:2px}
.hero-text h1{font-family:'Montserrat',Arial,sans-serif;font-size:78px;font-weight:500;letter-spacing:2px;line-height:1.05;margin-top:6px}
.btn{display:inline-block;background:var(--navy);color:var(--white);font-family:'Montserrat',Arial,sans-serif;font-weight:700;font-size:15px;padding:14px 22px;letter-spacing:.5px}
.hero-text .btn{margin-top:36px}

/* who */
.who{height:620px;position:relative}
.who-art{position:absolute;left:120px;top:80px;width:400px;height:440px}
.who-copy{position:absolute;left:664px;top:128px;width:440px}
.who-copy h2{font-family:'Montserrat',Arial,sans-serif;color:var(--teal);font-size:38px;font-weight:700}
.who-copy h3{font-family:'Montserrat',Arial,sans-serif;color:var(--ink);font-size:19px;font-weight:700;margin-top:14px}
.who-copy p{font-size:16px;line-height:1.75;margin-top:30px;color:var(--text)}
.who-copy .btn{margin-top:34px;font-size:14px}

/* features */
.features{height:460px;background:var(--grey-bg);display:flex;justify-content:center;gap:48px;padding-top:120px}
.feature{width:200px;text-align:center}
.feature .ring{width:160px;height:160px;border-radius:50%;border:2px solid var(--teal);background:var(--white);margin:0 auto;display:flex;align-items:center;justify-content:center}
.feature p{margin-top:28px;font-size:15px;line-height:1.5;color:var(--ink)}

/* blog */
.blog{height:780px;padding-top:130px}
.blog h2{text-align:center;font-family:'Montserrat',Arial,sans-serif;font-weight:700;font-size:42px;color:var(--teal)}
.cards{display:flex;justify-content:center;gap:24px;margin-top:58px}
.card{width:312px;background:var(--white);box-shadow:0 4px 18px rgba(0,0,0,.1);border-bottom:4px solid var(--teal)}
.card .photo{height:212px}
.card .body{padding:20px 26px 20px}
.card .date{display:flex;align-items:center;gap:8px;font-size:14px;color:var(--text)}
.card h4{font-family:'Montserrat',Arial,sans-serif;font-weight:700;font-size:21px;line-height:1.3;color:var(--ink);margin-top:12px}
.card p{font-size:14px;line-height:1.55;margin-top:12px;color:var(--text)}
.card .more{display:inline-block;margin-top:14px;font-family:'Montserrat',Arial,sans-serif;font-weight:700;font-size:14px;color:var(--ink);border-bottom:2px solid var(--ink);padding-bottom:2px}

/* newsletter */
.newsletter{height:340px;background:var(--navy);position:relative;overflow:hidden}
.newsletter .photo{position:absolute;right:0;top:0;width:300px;height:100%;clip-path:polygon(40% 0,100% 0,100% 100%,0 100%);background:linear-gradient(160deg,#dfe7ef 0%,#9fb3c8 50%,#4f6787 100%)}
.newsletter h2{position:absolute;left:344px;top:80px;font-family:'Montserrat',Arial,sans-serif;color:var(--white);font-weight:700;font-size:40px;letter-spacing:.5px}
.subscribe{position:absolute;left:168px;top:168px;display:flex;gap:24px}
.subscribe .field{width:592px;height:64px;background:var(--white);display:flex;align-items:center;padding-left:26px;font-size:15px;color:#8a909a}
.subscribe .go{width:248px;height:64px;background:var(--teal);color:var(--white);font-family:'Montserrat',Arial,sans-serif;font-weight:700;font-size:18px;display:flex;align-items:center;justify-content:center}

/* footer */
.footer{height:300px;background:var(--footer);padding:60px 112px 0;display:flex;color:#c9ccd1}
.footer .brand{width:396px}
.footer .brand .logo{color:var(--white);font-size:28px}
.footer .brand .social{display:flex;gap:12px;margin-top:34px}
.footer .brand .social span{width:30px;height:30px;border-radius:50%;background:var(--teal)}
.footer .col h5{font-family:'Montserrat',Arial,sans-serif;color:var(--white);font-size:19px;font-weight:700;margin-bottom:14px}
.footer .col ul{list-style:none}
.footer .col li{font-size:14px;line-height:1.9;display:flex;align-items:center;gap:10px}
.footer .col li::before{content:"";width:6px;height:6px;border-top:2px solid var(--teal);border-right:2px solid var(--teal);transform:rotate(45deg)}
.footer .links{width:180px}
.footer .company{width:212px}
.footer .contact li::before{display:none}
.footer .contact li{align-items:flex-start;line-height:1.5;margin-bottom:10px}
.footer .contact svg{flex:none;margin-top:2px}
.bottom-bar{height:60px;background:var(--footer-bar);color:#c9ccd1;font-size:14px;display:flex;align-items:center;justify-content:center;gap:10px}
</style>
</head>
<body>

<div class="topbar">
  <div class="contact">
    <svg width="16" height="16" viewBox="0 0 24 24" fill="#fff"><path d="M6.6 10.8a15.1 15.1 0 0 0 6.6 6.6l2.2-2.2a1 1 0 0 1 1-.25 11.4 11.4 0 0 0 3.6.57 1 1 0 0 1 1 1V20a1 1 0 0 1-1 1A17 17 0 0 1 3 4a1 1 0 0 1 1-1h3.5a1 1 0 0 1 1 1c0 1.25.2 2.45.57 3.57a1 1 0 0 1-.25 1z"/></svg>
    <span>978-XXX-XXXX</span>
  </div>
  <div class="sep"></div>
  <div class="contact">
    <svg width="17" height="14" viewBox="0 0 24 18" fill="#fff"><path d="M0 0h24v18H0z" fill="none"/><path d="M1 1h22v16H1z" fill="#fff"/><path d="M1 1l11 8 11-8" stroke="#15a6bd" stroke-width="2" fill="none"/></svg>
    <span>info@corvanti.com</span>
  </div>
  <div class="social"><span></span><span></span><span></span><span></span></div>
</div>

<nav class="nav">
  <div class="logo"><span class="dot"></span>Corvanti, LLC</div>
  <div class="menu">
    <span class="active">HOME</span>
    <span>ABOUT US</span>
    <span>SERVICES</span>
    <span>BLOG</span>
    <span>CONTACT</span>
    <svg width="22" height="22" viewBox="0 0 24 24" fill="none" stroke="#1f2a3c" stroke-width="3"><circle cx="10" cy="10" r="7"/><path d="M15 15l7 7"/></svg>
  </div>
</nav>

<section class="hero" role="img" aria-label="Healthcare professional reviewing billing data on a tablet">
  <div class="hero-text">
    <div class="pre">WELCOME TO</div>
    <h1>CORVANTI LLC</h1>
    <span class="btn">GET STARTED</span>
  </div>
</section>

<section class="who">
  <svg class="who-art" viewBox="0 0 400 440" role="img" aria-label="Illustration of a handshake framed within a medical cross">
    <defs><linearGradient id="crossGrad" x1="0" y1="0" x2="1" y2="1"><stop offset="0" stop-color="#9fb0c4"/><stop offset="1" stop-color="#3d5a80"/></linearGradient></defs>
    <path d="M130 0h140v150h130v140H270v150H130V290H0V150h130z" fill="url(#crossGrad)"/>
  </svg>
  <div class="who-copy">
    <h2>WHO ARE WE?</h2>
    <h3>CORVANTI LLC</h3>
    <p>We are a Northeast Arkansas medical billing and consulting company dedicated to providing efficient revenue cycle management and customer service with no interruption of cash flow to our clients. We handle maintaining the workflow of claim submissions to let provider's focus on patient care.</p>
    <span class="btn">LEARN MORE</span>
  </div>
</section>

<section class="features">
  <div class="feature">
    <div class="ring"><svg width="70" height="70" viewBox="0 0 64 64" fill="none" stroke="#1d2f5e" stroke-width="2.5"><rect x="14" y="10" width="36" height="46" rx="3"/><rect x="24" y="6" width="16" height="8" rx="2" fill="#8fd7e3"/><path d="M21 26l3 3 5-5M21 38l3 3 5-5"/><path d="M33 27h10M33 39h10" stroke="#15a6bd"/></svg></div>
    <p>HIPAA Compliant</p>
  </div>
  <div class="feature">
    <div class="ring"><svg width="70" height="70" viewBox="0 0 64 64" fill="none" stroke="#1d2f5e" stroke-width="2.5"><rect x="14" y="8" width="32" height="44" rx="2"/><path d="M20 18h20M20 26h20M20 34h12" stroke="#15a6bd"/><circle cx="44" cy="44" r="9" fill="#8fd7e3"/><path d="M40 52l-2 8 6-3 6 3-2-8"/></svg></div>
    <p>Credentialing and Credentialing Maintenance</p>
  </div>
  <div class="feature">
    <div class="ring"><svg width="70" height="70" viewBox="0 0 64 64" fill="none" stroke="#1d2f5e" stroke-width="2.5"><circle cx="36" cy="20" r="12" fill="#8fd7e3"/><path d="M36 13v14M32 17h6a3 3 0 0 1 0 6h-4"/><path d="M6 44h10l10 4h12a3 3 0 0 0 0-6H28M38 46l14-6a3 3 0 0 1 3 5L38 54H16"/></svg></div>
    <p>Pay Only for the Service You Need Rather than an Employee You Might Not Need</p>
  </div>
  <div class="feature">
    <div class="ring"><svg width="70" height="70" viewBox="0 0 64 64" fill="none" stroke="#1d2f5e" stroke-width="2.5"><circle cx="32" cy="18" r="7" fill="#8fd7e3"/><circle cx="14" cy="24" r="5"/><circle cx="50" cy="24" r="5"/><path d="M20 44c0-8 5-14 12-14s12 6 12 14zM4 44c0-6 4-10 10-10M60 44c0-6-4-10-10-10"/></svg></div>
    <p>Minimize Cash Flow Interruptions Caused by Employed Billers are Off</p>
  </div>
</section>

<section class="blog">
  <h2>LATEST FROM THE BLOG</h2>
  <div class="cards">
    <article class="card">
      <div class="photo" role="img" aria-label="Billing specialist working at a computer" style="background:linear-gradient(135deg,#e9eef2,#b7c6d3 60%,#8aa0b4)"></div>
      <div class="body">
        <div class="date"><svg width="14" height="14" viewBox="0 0 24 24" fill="none" stroke="#5d6675" stroke-width="2"><circle cx="12" cy="12" r="10"/><path d="M12 6v6l4 2"/></svg>October 25,2023</div>
        <h4>Sed ut perspiciatis unde omnis iste natus error sit</h4>
        <p>Lorem ipsum dolor sit amet, elit, sed do eiusmod tempor incididunt labore et dolore magna aliqua.</p>
        <span class="more">Learn More</span>
      </div>
    </article>
    <article class="card">
      <div class="photo" role="img" aria-label="Hands reviewing medical invoices with a calculator" style="background:linear-gradient(135deg,#f1efec,#d6cfc6 55%,#a9b7c2)"></div>
      <div class="body">
        <div class="date"><svg width="14" height="14" viewBox="0 0 24 24" fill="none" stroke="#5d6675" stroke-width="2"><circle cx="12" cy="12" r="10"/><path d="M12 6v6l4 2"/></svg>October 25,2023</div>
        <h4>Sed ut perspiciatis unde omnis iste natus error sit</h4>
        <p>Lorem ipsum dolor sit amet, elit, sed do eiusmod tempor incididunt labore et dolore magna aliqua.</p>
        <span class="more">Learn More</span>
      </div>
    </article>
    <article class="card">
      <div class="photo" role="img" aria-label="Smiling healthcare worker in a clinic" style="background:linear-gradient(135deg,#d9e6ea,#9ec3cd 55%,#5c93a3)"></div>
      <div class="body">
        <div class="date"><svg width="14" height="14" viewBox="0 0 24 24" fill="none" stroke="#5d6675" stroke-width="2"><circle cx="12" cy="12" r="10"/><path d="M12 6v6l4 2"/></svg>October 25,2023</div>
        <h4>Sed ut perspiciatis unde omnis iste natus error sit</h4>
        <p>Lorem ipsum dolor sit amet, elit, sed do eiusmod tempor incididunt labore et dolore magna aliqua.</p>
        <span class="more">Learn More</span>
      </div>
    </article>
  </div>
</section>

<section class="newsletter">
  <div class="photo" role="img" aria-label="Stethoscope resting on medical paperwork"></div>
  <h2>SIGN UP OUR NEWSLETTER</h2>
  <div class="subscribe">
    <div class="field">Enter your E - mail</div>
    <div class="go">SUBSCRIBE</div>
  </div>
</section>

<footer class="footer">
  <div class="brand">
    <div class="logo"><span class="dot"></span>Corvanti, LLC</div>
    <div class="social"><span></span><span></span><span></span><span></span></div>
  </div>
  <div class="col links">
    <h5>Quick Links</h5>
    <ul><li>Home</li><li>About Us</li><li>Services</li><li>Blog</li><li>Contact</li></ul>
  </div>
  <div class="col company">
    <h5>Our Company</h5>
    <ul><li>Terms &amp; Conditions</li><li>Privacy Policy</li><li>About Us</li><li>Support</li></ul>
  </div>
  <div class="col contact">
    <h5>Contact us</h5>
    <ul>
      <li><svg width="14" height="18" viewBox="0 0 24 30" fill="#fff"><path d="M12 0a11 11 0 0 0-11 11c0 8 11 19 11 19s11-11 11-19A11 11 0 0 0 12 0zm0 15a4 4 0 1 1 0-8 4 4 0 0 1 0 8z"/></svg>Lorem ipsum dolor sit<br>amet, consectetur</li>
      <li><svg width="14" height="14" viewBox="0 0 24 24" fill="#fff"><path d="M6.6 10.8a15.1 15.1 0 0 0 6.6 6.6l2.2-2.2a1 1 0 0 1 1-.25 11.4 11.4 0 0 0 3.6.57 1 1 0 0 1 1 1V20a1 1 0 0 1-1 1A17 17 0 0 1 3 4a1 1 0 0 1 1-1h3.5a1 1 0 0 1 1 1c0 1.25.2 2.45.57 3.57a1 1 0 0 1-.25 1z"/></svg>+1 (888) 888 8888</li>
      <li><svg width="15" height="12" viewBox="0 0 24 18"><path d="M1 1h22v16H1z" fill="#fff"/><path d="M1 1l11 8 11-8" stroke="#0d0f12" stroke-width="2" fill="none"/></svg>info@corvanti-llc.com</li>
    </ul>
  </div>
</footer>
<div class="bottom-bar"><span>©Copyrights 2023 Corvanti-llc</span><span>|</span><span>All Rights Reserved</span></div>

</body>
</html>
```